Redesign Current Website Into An Exciting Updated Design

We need to redesign the current website www.glintvaultoffers.net We want an overall new look. We are rebranding so it will be a new logo and we would like to see new images as well so you cannot compare the old from the new.

You can use same exact content as on current url www.glintvaultoffers.net

The website must be warm and inviting and fun yet professional and modern.

The website must also be designed with mobile in mind

The website must be warm and inviting yet professional and modern.

The website must also be designed with mobile in mind.

Target Market(s)

Consumers redeeming rewards

Industry/Entity Type

Promotional Reward Fullfillment

Coding

Coded - Design and coding required

Number of Pages Required

3 page

Requirements
Must have
• This website is a website where consumers come to redeem rewards they received from doing business with a company that offers these rewards. So the website should be very inviting.
Nice to have
• open
Should not have
• open

```html
<!DOCTYPE html>
<html lang="en">
<head>
<meta charset="utf-8">
<title>Glintvault Offers – Online Redemption System</title>
<link href="https://fonts.googleapis.com/css2?family=Plus+Jakarta+Sans:wght@400;500;600;700;800&display=swap" rel="stylesheet">
<style>
:root{
  --blue:#0b669d;
  --blue-deep:#0a5687;
  --blue-bright:#0b78c9;
  --blue-top:#0a6296;
  --ink:#111418;
  --muted:#5b6168;
  --tile:#f3f5f8;
  --field:#f4f5f7;
  --line:rgba(0,0,0,.05);
  --white:#ffffff;
  --star:#f5a623;
  --alert:#e8473b;
}
*{box-sizing:border-box;margin:0;padding:0}
html,body{width:1200px;height:1200px;overflow:hidden;background:var(--white)}
body{font-family:"Plus Jakarta Sans",sans-serif;color:var(--ink);position:relative}
.panel{position:absolute;top:0;height:1200px;overflow:hidden;background:var(--white)}
.panel--overview{left:0;width:371px}
.panel--overview .page{transform:scale(.4661);transform-origin:0 0}
.panel--detail{left:404px;width:796px}
.page{position:relative;width:796px;height:2571px;background:var(--white)}
.guide{position:absolute;top:22px;width:1px;height:1490px;background:var(--line)}
.abs{position:absolute}

.topbar{position:absolute;left:0;top:0;width:796px;height:22px;background:var(--blue-top);color:#fff;font-size:7.5px;display:flex;align-items:center;justify-content:center}
.nav{position:absolute;top:53px;left:107px;display:flex;gap:27px;font-size:7.5px;font-weight:500}
.brand{position:absolute;color:var(--blue);font-weight:800;text-transform:uppercase;text-align:center;line-height:.95;letter-spacing:.02em}
.brand--head{left:364px;top:40px;width:68px;font-size:11px}
.help-btn{position:absolute;left:619px;top:47px;width:70px;height:22px;border-radius:11px;background:var(--blue);color:#fff;font-size:8px;font-weight:600;display:flex;align-items:center;justify-content:center}

.eyebrow{position:absolute;font-size:6.6px;font-weight:700;color:var(--blue);text-transform:uppercase;padding-left:6px;border-left:1.5px solid var(--blue);line-height:9px}
.hero-title{position:absolute;left:122px;top:144px;font-size:24.5px;font-weight:700;line-height:32px;letter-spacing:-.02em}
.hero-copy{position:absolute;left:122px;top:217px;width:275px;font-size:9.2px;line-height:15.7px;color:var(--muted)}
.field{position:absolute;left:122px;width:272px;height:14px;background:var(--field);font-size:9.4px;color:var(--blue);padding-left:4px;line-height:14px}
.field-badge{position:absolute;right:8px;top:2px;width:10px;height:10px;border-radius:2px;background:var(--alert)}
.go-btn{position:absolute;left:122px;top:343px;width:45px;height:26px;border-radius:13px;background:var(--blue);color:#fff;font-size:8.6px;display:flex;align-items:center;justify-content:center}
.hero-art{position:absolute;left:403px;top:124px;width:261px;height:289px;border-radius:4px;background:linear-gradient(160deg,#e9eef3 0%,#ffffff 45%,#dbe8f5 75%,#1e6fc9 100%)}

.picks-title{position:absolute;left:0;width:796px;top:441px;text-align:center;font-size:12.4px;font-weight:600;color:var(--blue);letter-spacing:-.01em}
.pick{position:absolute;top:467px;width:109px;height:90px;background:var(--tile);border-radius:4px;text-align:center;color:var(--blue);font-size:7.6px;font-weight:600;line-height:11px}
.pick svg{display:block;margin:15px auto 19px}

.clients{position:absolute;left:0;top:612px;width:796px;height:191px;background:var(--blue);color:#fff;text-align:center}
.clients h2{position:absolute;top:45px;width:100%;font-size:12.4px;font-weight:600}
.clients p{position:absolute;top:65px;width:100%;font-size:7.4px}
.logo-strip{position:absolute;left:107px;top:107px;width:582px;height:39px;background:#fff;display:flex}
.logo-strip span{flex:1;display:flex;align-items:center;justify-content:center;border-right:1px solid #d9dde2;color:var(--ink);font-size:9px;font-weight:700}
.logo-strip span:last-child{border-right:none}

.about-copy{position:absolute;left:107px;top:942px;width:288px;font-size:7.9px;line-height:13.8px;color:var(--blue)}
.about-copy p{margin-bottom:7px}
.photo{position:absolute;left:479px;width:173px}

.cta{position:absolute;left:0;top:1533px;width:796px;height:179px;background:linear-gradient(90deg,var(--blue) 0%,var(--blue-bright) 100%);color:#fff}
.cta h3{position:absolute;left:107px;top:65px;width:260px;font-size:17px;font-weight:600;line-height:24px}
.cta p{position:absolute;left:462px;top:50px;width:230px;font-size:8px;line-height:16px}
.cta-btn{position:absolute;left:462px;top:110px;width:133px;height:24px;border-radius:12px;background:#fff;color:var(--blue);font-size:7.4px;display:flex;align-items:center;justify-content:center;gap:5px}

.voices{position:absolute;left:0;top:1712px;width:796px;height:591px;background:var(--blue);color:#fff}
.voices .tag{position:absolute;left:128px;top:66px;font-size:6px;font-weight:700}
.voices h3{position:absolute;left:122px;top:82px;font-size:22px;font-weight:600;letter-spacing:-.02em}
.voices .lede{position:absolute;left:422px;top:70px;width:250px;font-size:8px;line-height:16px}
.quote{position:absolute;width:169px;background:#fff;border-radius:3px;color:var(--ink);padding:16px 16px;font-size:8.6px;line-height:17.7px}
.stars{color:var(--star);font-size:8px;letter-spacing:2px;margin-bottom:10px}
.stars b{color:var(--muted);font-weight:500;letter-spacing:0;margin-left:3px}
.quote .who{font-weight:700;font-size:7.8px;margin-top:8px}

.footer{position:absolute;left:0;top:2303px;width:796px;height:268px;background:var(--blue-deep);color:#fff}
.ribbon-art{position:absolute;left:0;top:80px;width:796px;height:93px;background:linear-gradient(180deg,#0a3fb0,#1a57e0 50%,#0a3fb0)}
.bow-art{position:absolute;left:330px;top:0;width:270px;height:268px;background:radial-gradient(ellipse at center,#1c5be6 0%,#0b36a8 55%,rgba(11,54,168,0) 72%)}
.brand--foot{left:93px;top:97px;width:93px;font-size:16px;color:#fff}
.foot-links{position:absolute;top:93px;font-size:8.6px;line-height:21px}
.follow{position:absolute;left:93px;top:195px;display:flex;align-items:center;gap:14px;font-size:7.6px}
.follow i{display:block;width:9px;height:9px;border-radius:2px;background:#fff}
</style>
</head>
<body>

<!-- Full-page overview -->
<section class="panel panel--overview" aria-label="Full page overview">
  <div class="page">
    <div class="guide" style="left:107px"></div><div class="guide" style="left:689px"></div>
    <div class="topbar">🎉 Because you're special, here's a reward made just for you! ✨</div>
    <nav class="nav"><span>Service</span><span>Why Us</span><span>Testimonial</span><span>FAQ</span></nav>
    <div class="brand brand--head">Glintvault<br>Offers</div>
    <div class="help-btn">Need Help?</div>

    <div class="eyebrow" style="left:122px;top:126px">Promos and Rewards</div>
    <h1 class="hero-title">Welcome to the Online<br>Redemption System</h1>
    <p class="hero-copy">To Learn More About Your Offer Including The Full Details, How It Works, Terms, FAQ's and To Redeem and Activate Your Certificate Please Enter A Valid Certificate Number and Email.</p>
    <div class="field" style="top:288px">Your Name<span class="field-badge"></span></div>
    <div class="field" style="top:317px">example@email.com</div>
    <div class="go-btn">GO</div>
    <div class="hero-art" role="img" aria-label="Gift card with airplane and blue ribbon bow"></div>

    <div class="picks-title">Right here, right now—check this out!</div>
    <div class="pick" style="left:107px"><svg width="22" height="26" viewBox="0 0 22 26"><rect x="1" y="1" width="20" height="24" rx="2" fill="#0b669d"/><circle cx="11" cy="11" r="5" fill="none" stroke="#fff" stroke-width="1.5"/><path d="M6 11h10M11 6v10" stroke="#fff" stroke-width="1.2"/></svg>Vacation Certificates</div>
    <div class="pick" style="left:226px"><svg width="26" height="20" viewBox="0 0 26 20"><rect x="1" y="2" width="24" height="16" rx="3" fill="#0b669d"/><rect x="6" y="6" width="14" height="8" rx="1" fill="none" stroke="#fff" stroke-width="1.5"/></svg>Travel Vouchers</div>
    <div class="pick" style="left:344px"><svg width="26" height="22" viewBox="0 0 26 22"><rect x="3" y="2" width="20" height="14" fill="none" stroke="#0b669d" stroke-width="2.2"/><rect x="0" y="17" width="26" height="3" fill="#0b669d"/></svg>Digital Electronic<br>Products</div>
    <div class="pick" style="left:462px"><svg width="24" height="22" viewBox="0 0 24 22"><path d="M3 2h7l-1 8a3 3 0 0 1-5 0zM14 2h7l-1 8a3 3 0 0 1-5 0z" fill="#0b669d"/><path d="M6 12l-2 8M17 12l2 8" stroke="#0b669d" stroke-width="2"/></svg>Dining Incentives</div>
    <div class="pick" style="left:580px"><svg width="24" height="26" viewBox="0 0 24 26"><rect x="2" y="2" width="12" height="22" rx="2" fill="#0b669d"/><rect x="5" y="5" width="6" height="6" fill="#fff"/><path d="M14 8l5 3v10a2 2 0 0 0 4 0V9" fill="none" stroke="#0b669d" stroke-width="2"/></svg>Gas &amp; Grocery<br>Rewards</div>

    <section class="clients">
      <h2>Our Clients</h2>
      <p>A few of our clients that we redeem and fulfill gift certificates and rewards for</p>
      <div class="logo-strip"><span>Northcart</span><span>Steadfield</span><span>Bidloop</span><span>Corvane</span><span>Homeward Mutual</span><span>Skyrelay</span></div>
    </section>

    <div class="eyebrow" style="left:107px;top:925px">About Us</div>
    <div class="about-copy">
      <p>We provide marketing incentives in the form of gift certificates and vouchers that are redeemable for a variety of items such as: discount travel, smart device products, restaurant incentives , golf discounts and more to thousands of businesses around the world who use them to create exciting marketing promotions and giveaways, customer loyalty programs, promotional contests and use them as customer appreciation gifts.</p>
      <p>We are simply a 3rd party administrator that handles the redemption and fulfillment processing for a variety of incentive gifts and rewards. We have created the platform that facilitates the redemption and fulfillment process in a comprehensive, an easy to use online interface. Simply enter your code and email to redeem your offer and follow the steps to complete the fulfillment process to receive your gift. We work with thousands of large corporations and even small independently owned businesses that trust us to take care of their customers. It's our goal to make it easy for you to redeem your offer.</p>
      <p>We never market or distribute our incentives to end users as our business model is selling them to businesses and they distribute them to their customers through creative marketing strategies. The only way the recipient can get their hands on one of the certificates and vouchers is by participating in a promotion from one of the thousands of businesses around the world that currently use our marketing incentives in their advertising efforts.</p>
      <p>Since we do not ever distribute certificates to end users and only facilitate the redemption and fulfillment process, we can only honor what is stated in the terms and conditions of the offer. Be sure to read all the details, terms and frequently asked questions regarding your offer to better understand how your offer works. Our vendors, whom we contract with to make these offers happen are responsible for providing the specific terms and conditions in order to use the offer and we simply play as a middle man and a 3rd party administrator to facilitate the fulfillment process while enforcing the requirements. If you ever need to get a hold of us, simply login to the website by entering your certificate number and email at the top of this page and then by clicking on the red Support tab located in the lower right hand corner of your dashboard. We look forward to facilitating the process from start to finish.</p>
    </div>
    <div class="photo" style="top:865px;height:195px;background:linear-gradient(180deg,#c9d3dc,#8d9a95)" role="img" aria-label="Couple on a Paris balcony near the Eiffel Tower"></div>
    <div class="photo" style="top:1070px;height:194px;background:linear-gradient(180deg,#9fb2c2,#dfe3e6)" role="img" aria-label="Smiling man holding travel tickets"></div>
    <div class="photo" style="top:1275px;height:195px;background:linear-gradient(180deg,#a7b0b4,#c7a979)" role="img" aria-label="Older couple toasting with wine glasses"></div>

    <section class="cta">
      <h3>Surprises await! Redeem your exclusive rewards now!</h3>
      <p>We work with thousands of large corporations and even small independently owned businesses that trust us to take care of their customers.</p>
      <div class="cta-btn">Redeem Your Offer Now <svg width="5" height="7" viewBox="0 0 5 7"><path d="M1 1l2.5 2.5L1 6" fill="none" stroke="#0b669d" stroke-width="1"/></svg></div>
    </section>

    <section class="voices">
      <div class="tag">TESTIMONIALS</div>
      <h3>What they say about us</h3>
      <p class="lede">Our open, positive, and proactive approach helps us find ways to align your work environment with the culture and attitude you and your team aspire.</p>
      <div class="quote" style="left:126px;top:149px"><div class="stars">★★★★★<b>5.0</b></div>This course changed my whole concept regarding Landing Pages.<div class="who">Mira Holt, London</div></div>
      <div class="quote" style="left:126px;top:294px"><div class="stars">★★★★☆<b>4.5</b></div>This course is amazing 👋 I didn't expect this so much of great information! Our open, positive, and proactive approach helps us find ways to align your work environment.<div class="who">Dane Kerrow, Bangkok</div></div>
      <div class="quote" style="left:313px;top:149px"><div class="stars">★★★★★<b>5.0</b></div>This course is amazing 👋 I didn't expect this so much of great information! Our open, positive, and proactive approach helps us find ways to align your work environment with the culture and attitude you and your team aspire.<div class="who">Paul Averin, New York</div></div>
      <div class="quote" style="left:313px;top:400px"><div class="stars">★★★★★<b>5.0</b></div>This course is amazing 👋 I didn't expect this so much of great information!<div class="who">Mira Holt, London</div></div>
      <div class="quote" style="left:500px;top:149px"><div class="stars">★★★★☆<b>4.5</b></div>So many insights, new information, ways to align your work environment. loved the tips about landing page.<div class="who">Dane Kerrow, Bangkok</div></div>
      <div class="quote" style="left:500px;top:311px"><div class="stars">★★★★☆<b>4.5</b></div>This course is amazing 👋 I didn't expect this so much.<div class="who">Paul Averin, New York</div></div>
    </section>

    <footer class="footer">
      <div class="ribbon-art" role="img" aria-label="Blue satin ribbon band"></div>
      <div class="bow-art" role="img" aria-label="Large blue ribbon bow"></div>
      <div class="brand brand--foot">Glintvault<br>Offers</div>
      <div class="foot-links" style="left:389px">Home<br>Why Us<br>Deals</div>
      <div class="foot-links" style="left:498px">Service<br>Case Studies<br>Plan</div>
      <div class="foot-links" style="left:607px">Testimonial<br>About<br>FAQ</div>
      <div class="follow">Follow us on: <i></i><i></i><i></i><i></i></div>
    </footer>
  </div>
</section>

<!-- Detail view -->
<section class="panel panel--detail" aria-label="Page detail">
  <div class="page">
    <div class="guide" style="left:107px"></div><div class="guide" style="left:689px"></div>
    <div class="topbar">🎉 Because you're special, here's a reward made just for you! ✨</div>
    <nav class="nav"><span>Service</span><span>Why Us</span><span>Testimonial</span><span>FAQ</span></nav>
    <div class="brand brand--head">Glintvault<br>Offers</div>
    <div class="help-btn">Need Help?</div>

    <div class="eyebrow" style="left:122px;top:126px">Promos and Rewards</div>
    <h1 class="hero-title">Welcome to the Online<br>Redemption System</h1>
    <p class="hero-copy">To Learn More About Your Offer Including The Full Details, How It Works, Terms, FAQ's and To Redeem and Activate Your Certificate Please Enter A Valid Certificate Number and Email.</p>
    <div class="field" style="top:288px">Your Name<span class="field-badge"></span></div>
    <div class="field" style="top:317px">example@email.com</div>
    <div class="go-btn">GO</div>
    <div class="hero-art" role="img" aria-label="Gift card with airplane and blue ribbon bow"></div>

    <div class="picks-title">Right here, right now—check this out!</div>
    <div class="pick" style="left:107px"><svg width="22" height="26" viewBox="0 0 22 26"><rect x="1" y="1" width="20" height="24" rx="2" fill="#0b669d"/><circle cx="11" cy="11" r="5" fill="none" stroke="#fff" stroke-width="1.5"/><path d="M6 11h10M11 6v10" stroke="#fff" stroke-width="1.2"/></svg>Vacation Certificates</div>
    <div class="pick" style="left:226px"><svg width="26" height="20" viewBox="0 0 26 20"><rect x="1" y="2" width="24" height="16" rx="3" fill="#0b669d"/><rect x="6" y="6" width="14" height="8" rx="1" fill="none" stroke="#fff" stroke-width="1.5"/></svg>Travel Vouchers</div>
    <div class="pick" style="left:344px"><svg width="26" height="22" viewBox="0 0 26 22"><rect x="3" y="2" width="20" height="14" fill="none" stroke="#0b669d" stroke-width="2.2"/><rect x="0" y="17" width="26" height="3" fill="#0b669d"/></svg>Digital Electronic<br>Products</div>
    <div class="pick" style="left:462px"><svg width="24" height="22" viewBox="0 0 24 22"><path d="M3 2h7l-1 8a3 3 0 0 1-5 0zM14 2h7l-1 8a3 3 0 0 1-5 0z" fill="#0b669d"/><path d="M6 12l-2 8M17 12l2 8" stroke="#0b669d" stroke-width="2"/></svg>Dining Incentives</div>
    <div class="pick" style="left:580px"><svg width="24" height="26" viewBox="0 0 24 26"><rect x="2" y="2" width="12" height="22" rx="2" fill="#0b669d"/><rect x="5" y="5" width="6" height="6" fill="#fff"/><path d="M14 8l5 3v10a2 2 0 0 0 4 0V9" fill="none" stroke="#0b669d" stroke-width="2"/></svg>Gas &amp; Grocery<br>Rewards</div>

    <section class="clients">
      <h2>Our Clients</h2>
      <p>A few of our clients that we redeem and fulfill gift certificates and rewards for</p>
      <div class="logo-strip"><span>Northcart</span><span>Steadfield</span><span>Bidloop</span><span>Corvane</span><span>Homeward Mutual</span><span>Skyrelay</span></div>
    </section>

    <div class="eyebrow" style="left:107px;top:925px">About Us</div>
    <div class="about-copy">
      <p>We provide marketing incentives in the form of gift certificates and vouchers that are redeemable for a variety of items such as: discount travel, smart device products, restaurant incentives , golf discounts and more to thousands of businesses around the world who use them to create exciting marketing promotions and giveaways, customer loyalty programs, promotional contests and use them as customer appreciation gifts.</p>
      <p>We are simply a 3<sup>rd</sup> party administrator that handles the redemption and fulfillment processing for a variety of incentive gifts and rewards. We have created the platform that facilitates the redemption and fulfillment process in a comprehensive, an easy to use online interface. Simply enter your code and email to redeem your offer and follow the steps to complete the fulfillment process to receive your gift. We work with thousands of large corporations and even small independently owned businesses that trust us to take care of their customers. It's our goal to make it easy for you to redeem your offer.</p>
      <p>We never market or distribute our incentives to end users as our business model is selling them to businesses and they distribute them to their customers through creative marketing strategies. The only way the recipient can get their hands on one of the certificates and vouchers is by participating in a promotion from one of the thousands of businesses around the world.</p>
    </div>
    <div class="photo" style="top:865px;height:195px;background:linear-gradient(180deg,#c9d3dc,#8d9a95)" role="img" aria-label="Couple on a Paris balcony near the Eiffel Tower"></div>
    <div class="photo" style="top:1070px;height:194px;background:linear-gradient(180deg,#9fb2c2,#dfe3e6)" role="img" aria-label="Smiling man holding travel tickets"></div>
  </div>
</section>

</body>
</html>
```